I apologize on the fact that star rating on the same design will change during the contest. But you are making so many design, which is great :) , but make the selection quite difficult... Will do my best to give you information of what I like, but it will take some time...
Will it be possible to upload your creation without putting them like in 3D view. I am not comfortable to do a selection on design with a 60° of view angle ;)
And also if you can just have a neutral background around the card it will be more easy...
Just a small precision... In the Brief I describe that I would like a black or white background to see how it will look.
This white or black color has to be on the card itself as the "background" beside the logo (that's why I have put two logos) and not around the business card.
I have just uploaded a zip file containing all file formats for the logo.
Kind Regards,
Marc Delorme
Kind regards,

```html
<!DOCTYPE html>
<html lang="en">
<head>
<meta charset="utf-8">
<title>Soaring Systems – Stationery Concepts</title>
<link href="https://fonts.googleapis.com/css2?family=Exo+2:wght@400;700&display=swap" rel="stylesheet">
<style>
  :root {
    --bg-top: #55585c;
    --bg-bottom: #1c1d1f;
    --paper: #ffffff;
    --paper-shade: #eef1f4;
    --blue: #1c5fc0;
    --blue-dark: #0b2f78;
    --orange: #f08a12;
    --ink: #2b3a55;
    --caption: #c9ccd1;
  }
  * { box-sizing: border-box; margin: 0; padding: 0; }
  html, body { width: 1200px; height: 444px; overflow: hidden; }
  body {
    background: radial-gradient(ellipse at 50% 20%, var(--bg-top), var(--bg-bottom) 80%);
    font-family: "Exo 2", sans-serif;
    position: relative;
    color: var(--ink);
  }
  .brand-name { font-weight: 700; color: var(--orange); letter-spacing: .3px; white-space: nowrap; }
  .brand-dot { display: inline-block; border-radius: 50%; background: var(--blue); vertical-align: middle; }

  .intro { position: absolute; left: 24px; top: 34px; width: 168px; text-align: center; }
  .intro .brand-dot { width: 36px; height: 36px; display: block; margin: 0 auto 10px; }
  .intro .brand-name { font-size: 17px; }
  .intro-title { color: var(--paper); font-size: 12px; margin-top: 6px; }

  .piece { position: absolute; background: var(--paper); overflow: hidden; box-shadow: 0 3px 10px rgba(0,0,0,.5); }
  .wave { position: absolute; left: 0; bottom: 0; width: 100%; }
  .caption { position: absolute; color: var(--caption); font-size: 6px; text-align: center; }

  .business-card { left: 24px; top: 211px; width: 168px; height: 84px; }
  .business-card .card-name { position: absolute; left: 10px; top: 9px; font-size: 8px; font-weight: 700; color: var(--blue-dark); }
  .business-card .card-role { position: absolute; left: 10px; top: 20px; font-size: 5px; }
  .business-card .card-contact { position: absolute; right: 10px; bottom: 8px; font-size: 4.5px; text-align: right; line-height: 1.4; color: var(--paper); }

  .letterhead { top: 19px; width: 295px; height: 384px; }
  .letterhead-one { left: 199px; }
  .letterhead-two { left: 506px; }
  .letterhead .head-brand { position: absolute; top: 20px; font-size: 10px; }
  .letterhead-one .head-brand { left: 34px; }
  .letterhead-two .head-brand { left: 0; right: 0; text-align: center; }
  .letterhead .brand-dot { width: 11px; height: 11px; margin-right: 4px; }
  .letterhead .head-contact { position: absolute; top: 16px; left: 182px; font-size: 4px; line-height: 1.5; }
  .letterhead-two .head-contact { left: 0; width: 100%; top: 38px; text-align: center; }
  .letterhead .foot-address { position: absolute; bottom: 10px; right: 18px; font-size: 4px; line-height: 1.5; text-align: right; color: var(--paper); }

  .envelope { left: 828px; width: 360px; }
  .envelope .brand-name { position: absolute; font-size: 7px; }
  .envelope .brand-dot { width: 8px; height: 8px; margin-right: 3px; }
  .envelope-front-a { top: 40px; height: 62px; }
  .envelope-back-a { top: 108px; height: 78px; background: var(--paper-shade); }
  .envelope-back-b { top: 200px; height: 76px; background: var(--paper-shade); }
  .envelope-front-b { top: 272px; height: 66px; }
  .envelope .flap { position: absolute; inset: 0; width: 100%; height: 100%; }
</style>
</head>
<body>

<section class="intro">
  <span class="brand-dot"></span>
  <span class="brand-name">Soaring Systems</span>
  <p class="intro-title">Stationery Concepts</p>
</section>

<article class="piece business-card">
  <p class="card-name">Marc Delorme</p>
  <p class="card-role">Director</p>
  <svg class="wave" viewBox="0 0 168 50" preserveAspectRatio="none">
    <path d="M0 20 Q84 4 168 14 L168 50 L0 50Z" fill="var(--blue)"/>
    <path d="M0 17 Q84 1 168 11" stroke="var(--orange)" stroke-width="2" fill="none"/>
  </svg>
  <p class="card-contact">+41 22 555 01 20<br>marc@soaringsys.ch<br>www.soaringsys.ch</p>
</article>
<p class="caption" style="left:24px;top:305px;width:168px">Business Card</p>

<article class="piece letterhead letterhead-one">
  <p class="head-brand"><span class="brand-dot"></span><span class="brand-name">Soaring Systems</span></p>
  <p class="head-contact">+41 22 555 01 20<br>+41 22 555 01 21<br>info@soaringsys.ch<br>www.soaringsys.ch</p>
  <svg class="wave" viewBox="0 0 295 60" preserveAspectRatio="none">
    <path d="M0 34 Q148 10 295 24 L295 60 L0 60Z" fill="var(--blue)"/>
    <path d="M0 30 Q148 6 295 20" stroke="var(--orange)" stroke-width="2.5" fill="none"/>
  </svg>
  <p class="foot-address">Rue du Lac 12<br>1200 Geneva</p>
</article>
<p class="caption" style="left:199px;top:410px;width:295px">Letterhead option 1</p>

<article class="piece letterhead letterhead-two">
  <p class="head-brand"><span class="brand-dot"></span><span class="brand-name">Soaring Systems</span></p>
  <p class="head-contact">+41 22 555 01 20 · info@soaringsys.ch · www.soaringsys.ch</p>
  <svg class="wave" viewBox="0 0 295 60" preserveAspectRatio="none">
    <path d="M0 24 Q148 42 295 20 L295 60 L0 60Z" fill="var(--blue)"/>
    <path d="M0 20 Q148 38 295 16" stroke="var(--orange)" stroke-width="2.5" fill="none"/>
  </svg>
  <p class="foot-address">Rue du Lac 12<br>1200 Geneva</p>
</article>
<p class="caption" style="left:506px;top:410px;width:295px">Letterhead option 2</p>

<article class="piece envelope envelope-front-a">
  <p class="brand-name" style="left:0;right:0;top:10px;text-align:center"><span class="brand-dot"></span>Soaring Systems</p>
  <svg class="wave" viewBox="0 0 360 24" preserveAspectRatio="none">
    <path d="M0 12 Q180 2 360 8 L360 24 L0 24Z" fill="var(--blue)"/>
    <path d="M0 10 Q180 0 360 6" stroke="var(--orange)" stroke-width="2" fill="none"/>
  </svg>
</article>

<article class="piece envelope envelope-back-a">
  <svg class="flap" viewBox="0 0 360 78" preserveAspectRatio="none">
    <path d="M0 0 H360 V30 L180 52 L0 30Z" fill="var(--orange)"/>
  </svg>
  <p class="brand-name" style="left:0;right:0;top:56px;text-align:center;color:var(--blue)"><span class="brand-dot"></span>Soaring Systems</p>
</article>

<article class="piece envelope envelope-back-b">
  <svg class="flap" viewBox="0 0 360 76" preserveAspectRatio="none">
    <path d="M0 0 L180 40 L360 0" stroke="#cfd5dc" fill="none"/>
  </svg>
  <p class="brand-name" style="left:0;right:0;top:14px;text-align:center"><span class="brand-dot"></span>Soaring Systems</p>
</article>

<article class="piece envelope envelope-front-b">
  <p class="brand-name" style="left:14px;top:10px"><span class="brand-dot"></span>Soaring Systems</p>
  <svg class="wave" viewBox="0 0 360 24" preserveAspectRatio="none">
    <path d="M0 14 Q180 4 360 10 L360 24 L0 24Z" fill="var(--blue)"/>
    <path d="M0 12 Q180 2 360 8" stroke="var(--orange)" stroke-width="2" fill="none"/>
  </svg>
</article>
<p class="caption" style="left:828px;top:345px;width:360px">Envelope – front &amp; back</p>

</body>
</html>
```